Business Card Design Project

I have a two letter domain name qo.com.au (lower case font please). I want a business card, cum logo that is die cut (around the qo segment at least) that fits standard business card size.
qo is all about what 'I am' - a journalist, blogger, analyst, commentator. My mantra is "I wander so qo'.
The reverse of the card only needs my name Lon Fitch, email lon@qo.com.au and mobile +61 400 555 817
Target Market(s)
Mainly people that will use my professional writing services and suppliers that will provide product for review
Industry/Entity Type
Business
Requirements
Must have
- One side is qo.com.au (hint - the .com.au can be vertical or horizontal to fit - the qo should be as large as possible).
The other requires large size font name, email and phone details (so no one needs glasses to read it).
The die cut can be just to highlight the qo segment - need not be around the whole card.
Font used in the past was Belwe (old style - very much like the i used in the information symbol).
Colours - no preference - prefer two colour to process colour but can also be an outline font instead of solid colour.

```html
<!DOCTYPE html>
<html lang="en">
<head>
<meta charset="utf-8">
<title>qo business card – Lon Fitch</title>
<link href="https://fonts.googleapis.com/css2?family=Cinzel:wght@700;900&family=Noto+Sans:wght@400;500&display=swap" rel="stylesheet">
<style>
  :root {
    --backdrop: #000000;
    --card-top: #ffffff;
    --card-mid: #eef1f1;
    --card-bottom: #c3cdcd;
    --ink: #121212;
    --mark-grey: #6d7778;
    --ornament: #3a3a3a;
  }
  * { margin: 0; padding: 0; box-sizing: border-box; }
  html, body {
    width: 1200px;
    height: 1092px;
    overflow: hidden;
    background: var(--backdrop);
  }
  .sheet {
    position: relative;
    width: 1200px;
    height: 1092px;
  }
  .card {
    position: absolute;
    top: 60px;
    width: 510px;
    height: 972px;
    background: linear-gradient(180deg, var(--card-top) 0%, var(--card-mid) 45%, var(--card-bottom) 100%);
  }
  .card--front { left: 60px; }
  .card--back { left: 630px; }

  /* Front: brand name */
  .brand {
    position: absolute;
    left: 0;
    right: 0;
    top: 472px;
    text-align: center;
    font-family: "Noto Sans", sans-serif;
    font-weight: 500;
    font-size: 330px;
    line-height: 1;
    color: var(--mark-grey);
    letter-spacing: -4px;
  }
  .brand-domain {
    position: absolute;
    right: 62px;
    top: 860px;
    font-family: "Noto Sans", sans-serif;
    font-weight: 500;
    font-size: 54px;
    line-height: 1;
    color: var(--mark-grey);
  }

  /* Back: contact details */
  .details {
    position: absolute;
    left: 0;
    right: 0;
    top: 258px;
    text-align: center;
    color: var(--ink);
    text-transform: uppercase;
  }
  .details__name {
    font-family: "Cinzel", serif;
    font-weight: 900;
    font-size: 52px;
    letter-spacing: 6px;
    line-height: 62px;
    white-space: nowrap;
    margin: 0 -10px 6px;
  }
  .details__name .sep { font-size: 40px; vertical-align: 4px; }
  .details__line {
    font-family: "Cinzel", serif;
    font-weight: 700;
    font-size: 32px;
    letter-spacing: 4px;
    line-height: 54.3px;
  }
  .details__value {
    font-family: "Noto Sans", sans-serif;
    font-weight: 400;
    font-size: 30px;
    letter-spacing: 1.5px;
    line-height: 54.3px;
    text-transform: none;
  }
  .ornament {
    display: block;
    margin: 6px auto 0;
    width: 150px;
    height: 22px;
    border-radius: 11px;
    background: linear-gradient(90deg, transparent 0%, var(--ornament) 30%, var(--ornament) 70%, transparent 100%);
    opacity: 0.55;
  }
</style>
</head>
<body>
<main class="sheet">
  <section class="card card--front" aria-label="Card front">
    <div class="brand">qo</div>
    <div class="brand-domain">.com.au</div>
  </section>

  <section class="card card--back" aria-label="Card back">
    <div class="details">
      <p class="details__name"><span class="sep">·</span>Lon Fitch<span class="sep">·</span></p>
      <p class="details__line">Journalist</p>
      <p class="details__line">Blogger</p>
      <p class="details__line">Analyst</p>
      <p class="details__line">Commentator</p>
      <p class="details__line">Email</p>
      <p class="details__value">lon@qo.com.au</p>
      <p class="details__line">Mobile</p>
      <p class="details__value">+61·400·555·817</p>
      <span class="ornament" role="img" aria-label="Decorative scroll flourish"></span>
    </div>
  </section>
</main>
</body>
</html>
```